Packaging for Portable Bidet Product

Product:
Our product, Swishka, is a portable hand bidet. What is a portable hand bidet as some may ask? It is small water bottle with a nozzle head that is used to wash “bottoms” after going “poo-poo” (pardon our crudeness). Bidets are popular in European, Asian and African markets and are used alongside toilet paper to give a truly fresh and clean experience. Besides cleanliness, bidets are eco-friendly (they reduce toilet paper usage by x%) and are perfect for travel.
Current Competition + Role of Packaging:
We are launching our portable bidet product in the US market, primarily to be sold via Marketvale. There are currently some existing players in the market, but we’ve done our research and created a product that is superior in functionality and style. That being said, our competitors still have a first-mover advantage and have amassed a high volume of Marketvale ratings, hence we have a bit of a challenge which we feel that can be easily tackled with premium branding and marketing.
That being said, we are looking for a packaging design that:
i. Distinguishing our product on Marketvale (meaning, the packaging looks good in photos)
ii. Highlight that ours is a premium product
Our design values:
‘Hygiene meets modern design’. Some adjectives that describe our brand -
• Clean
• Fresh
• Simple
• Quirky
• Premium
• Discreet
• Subtle
Attachments:
• Our packaging dimensions (see attached)
• Our brand color (Pantone 331C)
• Our logo file (see attached file)
• Product photos (see attached file)
• Illustration of our product instructions (see attached file)
• Packaging designs that inspire us (see attached file)
• Packaging designs of our competition for reference (see attached file)
• Content/text for the packaging box (see below)
What should be on the box:
• Logo and Brand Name
• Product Photo (can be an outline/illustration as well)
• Product instructions illustration (see attached file)
• Text to be included in packaging
o Product description – “A Modern Portable Bidet”
o Bottle size – 400ml
o Key features
Anti-leak
Discreet design
Travel friendly size
Angled spray
Eco-friendly
Easy squeeze bottle
Includes travel bag
Target Market(s)
The product is aimed at both men and women (of all ages) in the US and Canada markets. In terms of audience targets, we will be appealing to outdoor enthusiasts, immigrants abroad, new parents (product to be used to clean their babies), patients (people with limited mobility) and eco-conscious consumers.
Industry/Entity Type
Health And Wellness

```html
<!DOCTYPE html>
<html lang="en">
<head>
<meta charset="utf-8">
<title>Swishka – Packaging Panels</title>
<link rel="stylesheet" href="https://fonts.googleapis.com/css2?family=Nunito:wght@400;800&family=Oswald:wght@300;400&display=swap">
<style>
  :root {
    --bg: #e8ebed;
    --white: #ffffff;
    --mint: #a6dccf;
    --mint-deep: #93d2c2;
    --wave-1: #eaf6fa;
    --wave-2: #d3edf4;
    --wave-3: #b4e1ec;
    --wave-4: #93d3e2;
    --wave-5: #74c5d6;
    --ink: #1d2a2e;
    --icon-line: #ffffff;
  }
  * { box-sizing: border-box; margin: 0; padding: 0; }
  html, body { width: 1200px; height: 910px; overflow: hidden; background: var(--bg); }
  .canvas { position: relative; width: 1200px; height: 910px; }

  .panel {
    position: absolute; top: 35px; width: 292px; height: 840px;
    background: var(--white); overflow: hidden;
  }
  .panel--instructions { left: 306px; }
  .panel--front { left: 602px; }

  .panel__waves { position: absolute; inset: 0; width: 100%; height: 100%; }

  .brand-ring {
    position: absolute; left: 96px; top: 70px; width: 100px; height: 100px;
    border: 12px solid var(--mint); border-radius: 50%;
  }
  .wordmark {
    position: absolute; left: 0; right: 0; top: 232px; text-align: center;
    font-family: "Nunito", sans-serif; font-weight: 800; font-size: 44px;
    color: var(--mint); letter-spacing: -1px; line-height: 1;
  }
  .descriptor {
    position: absolute; left: 0; right: 0; top: 290px; text-align: center;
    font-family: "Nunito", sans-serif; font-weight: 400; font-size: 13.5px; color: var(--ink);
  }

  .step {
    position: absolute; width: 92px; height: 92px; border-radius: 50%;
    background: var(--white); border: 1px solid #e6f4f7;
  }
  .step__num {
    position: absolute; width: 24px; height: 24px; border-radius: 50%;
    background: var(--white); border: 1.5px solid var(--wave-3);
    font-family: "Nunito", sans-serif; font-size: 15px; color: var(--wave-4);
    display: flex; align-items: center; justify-content: center;
  }
  .step--1 { left: 35px; top: 441px; } .num--1 { left: 113px; top: 455px; }
  .step--2 { left: 149px; top: 441px; } .num--2 { left: 227px; top: 455px; }
  .step--3 { left: 35px; top: 551px; } .num--3 { left: 113px; top: 565px; }
  .step--4 { left: 149px; top: 551px; } .num--4 { left: 227px; top: 565px; }
  .step--5 { left: 92px; top: 659px; } .num--5 { left: 170px; top: 673px; }

  .easy-to-use {
    position: absolute; left: 0; right: 0; top: 773px; text-align: center;
    font-family: "Oswald", sans-serif; font-weight: 400; font-size: 14px;
    letter-spacing: 3px; color: var(--white);
  }

  .tagline-band {
    position: absolute; left: 0; right: 0; bottom: 0; height: 24px;
    background: var(--mint); display: flex; align-items: center; justify-content: center;
    font-family: "Nunito", sans-serif; font-size: 12.5px; letter-spacing: 3px; color: var(--white);
  }

  .product-photo {
    position: absolute; left: 92px; top: 318px; width: 108px; height: 498px;
    border-radius: 40px 40px 0 0;
    background: linear-gradient(180deg, #f4f6f7 0%, #f4f6f7 74%, #9fd8c4 74%, #8ecfb8 100%);
  }

  .feature {
    position: absolute; width: 90px; text-align: center;
    font-family: "Oswald", sans-serif; font-weight: 300; font-size: 7.5px;
    color: var(--white); letter-spacing: 0.2px; line-height: 1.2;
  }
  .feature svg { display: block; margin: 0 auto 2px; width: 32px; height: 32px; }
  .feature--left { left: -5px; }
  .feature--right { left: 199px; }

  .size-badge {
    position: absolute; left: 22px; top: 773px; width: 38px; height: 28px;
    border: 1.5px solid var(--white); border-radius: 6px;
    font-family: "Nunito", sans-serif; font-weight: 800; font-size: 5.5px; line-height: 1.15;
    color: var(--white); padding: 4px 0 0 14px;
  }
  .size-badge::before {
    content: ""; position: absolute; left: 5px; top: 5px; width: 5px; height: 16px;
    border-radius: 3px; background: var(--white);
  }
</style>
</head>
<body>
<main class="canvas">

  <!-- Instructions panel -->
  <section class="panel panel--instructions">
    <svg class="panel__waves" viewBox="0 0 292 840" preserveAspectRatio="none" aria-hidden="true">
      <path d="M0 160 C80 200 200 210 292 175 L292 840 L0 840 Z" fill="var(--wave-1)"/>
      <path d="M0 350 C60 335 110 370 160 380 C220 390 260 330 292 335 L292 840 L0 840 Z" fill="var(--wave-2)"/>
      <path d="M0 420 C70 400 140 445 200 430 C250 418 270 415 292 420 L292 840 L0 840 Z" fill="var(--wave-3)"/>
      <path d="M0 520 C80 495 150 540 220 525 C260 516 280 512 292 515 L292 840 L0 840 Z" fill="var(--wave-4)"/>
      <path d="M0 640 C80 610 170 660 292 630 L292 840 L0 840 Z" fill="var(--wave-5)"/>
    </svg>

    <div class="brand-ring" aria-hidden="true"></div>
    <div class="wordmark">swishka</div>
    <div class="descriptor">A Modern Portable Bidet</div>

    <div class="step step--1" role="img" aria-label="Step 1: fill the bottle with water from the tap"></div>
    <div class="step__num num--1">1</div>
    <div class="step step--2" role="img" aria-label="Step 2: pull the nozzle up out of the bottle"></div>
    <div class="step__num num--2">2</div>
    <div class="step step--3" role="img" aria-label="Step 3: squeeze the bottle to spray"></div>
    <div class="step__num num--3">3</div>
    <div class="step step--4" role="img" aria-label="Step 4: push the nozzle back down"></div>
    <div class="step__num num--4">4</div>
    <div class="step step--5" role="img" aria-label="Step 5: cap and store the bottle"></div>
    <div class="step__num num--5">5</div>

    <div class="easy-to-use">Easy to use</div>
    <div class="tagline-band">Hygiene meets modern design</div>
  </section>

  <!-- Front panel -->
  <section class="panel panel--front">
    <svg class="panel__waves" viewBox="0 0 292 840" preserveAspectRatio="none" aria-hidden="true">
      <path d="M0 160 C80 200 200 210 292 170 L292 840 L0 840 Z" fill="var(--wave-1)"/>
      <path d="M0 350 C60 335 110 370 160 380 C220 390 260 330 292 335 L292 840 L0 840 Z" fill="var(--wave-2)"/>
      <path d="M0 420 C70 400 140 445 200 430 C250 418 270 415 292 420 L292 840 L0 840 Z" fill="var(--wave-3)"/>
      <path d="M0 520 C80 495 150 540 220 525 C260 516 280 512 292 515 L292 840 L0 840 Z" fill="var(--wave-4)"/>
      <path d="M0 640 C80 610 170 660 292 630 L292 840 L0 840 Z" fill="var(--wave-5)"/>
    </svg>

    <div class="brand-ring" aria-hidden="true"></div>
    <div class="wordmark">swishka</div>
    <div class="descriptor">A Modern Portable Bidet</div>

    <div class="product-photo" role="img" aria-label="Product photo: white and mint portable bidet bottle with extended nozzle"></div>

    <div class="feature feature--left" style="top:616px">
      <svg viewBox="0 0 32 32" aria-hidden="true"><circle cx="16" cy="16" r="14" fill="none" stroke="#fff" stroke-width="1.6"/><path d="M16 8 C12 14 11 16 11 19 a5 5 0 0 0 10 0 C21 16 20 14 16 8Z" fill="#fff"/><line x1="7" y1="7" x2="25" y2="25" stroke="#fff" stroke-width="1.6"/></svg>
      ANTI-LEAK
    </div>
    <div class="feature feature--left" style="top:663px">
      <svg viewBox="0 0 32 32" aria-hidden="true"><circle cx="16" cy="16" r="14" fill="none" stroke="#fff" stroke-width="1.6"/><path d="M7 16 Q16 8 25 16 Q16 24 7 16Z" fill="none" stroke="#fff" stroke-width="1.6"/><circle cx="16" cy="16" r="3" fill="#fff"/><line x1="8" y1="24" x2="24" y2="8" stroke="#fff" stroke-width="1.6"/></svg>
      DISCREET DESIGN
    </div>
    <div class="feature feature--left" style="top:710px">
      <svg viewBox="0 0 32 32" aria-hidden="true"><circle cx="16" cy="16" r="14" fill="none" stroke="#fff" stroke-width="1.6"/><path d="M16 25 C11 19 10 16 10 13 a6 6 0 0 1 12 0 C22 16 21 19 16 25Z" fill="none" stroke="#fff" stroke-width="1.6"/><circle cx="16" cy="13" r="2" fill="#fff"/></svg>
      TRAVEL FRIENDLY SIZE
    </div>
    <div class="size-badge">BOTTLE<br>SIZE<br>400ml</div>

    <div class="feature feature--right" style="top:615px">
      <svg viewBox="0 0 32 32" aria-hidden="true"><circle cx="16" cy="16" r="14" fill="none" stroke="#fff" stroke-width="1.6"/><line x1="12" y1="10" x2="12" y2="26" stroke="#fff" stroke-width="1.6"/><circle cx="17" cy="10" r="1" fill="#fff"/><circle cx="20" cy="8" r="1" fill="#fff"/><circle cx="21" cy="12" r="1" fill="#fff"/><circle cx="24" cy="10" r="1" fill="#fff"/></svg>
      ANGLED SPRAY
    </div>
    <div class="feature feature--right" style="top:661px">
      <svg viewBox="0 0 32 32" aria-hidden="true"><circle cx="16" cy="16" r="14" fill="none" stroke="#fff" stroke-width="1.6"/><path d="M9 23 C9 14 15 9 24 9 C24 18 18 23 9 23Z" fill="#fff"/></svg>
      ECO-FRIENDLY
    </div>
    <div class="feature feature--right" style="top:708px">
      <svg viewBox="0 0 32 32" aria-hidden="true"><circle cx="16" cy="16" r="14" fill="none" stroke="#fff" stroke-width="1.6"/><rect x="13" y="9" width="6" height="15" rx="3" fill="#fff"/><line x1="5" y1="17" x2="11" y2="17" stroke="#fff" stroke-width="1.6"/><line x1="21" y1="17" x2="27" y2="17" stroke="#fff" stroke-width="1.6"/></svg>
      EASY SQUEEZE BOTTLE
    </div>
    <div class="feature feature--right" style="top:754px">
      <svg viewBox="0 0 32 32" aria-hidden="true"><circle cx="16" cy="16" r="14" fill="none" stroke="#fff" stroke-width="1.6"/><rect x="10" y="13" width="12" height="11" rx="2" fill="none" stroke="#fff" stroke-width="1.6"/><path d="M13 13 V10 a3 3 0 0 1 6 0 V13" fill="none" stroke="#fff" stroke-width="1.6"/></svg>
      INCLUDES TRAVEL BAG
    </div>

    <div class="tagline-band">Hygiene meets modern design</div>
  </section>

</main>
</body>
</html>
```